Corvena Card

The logo is the Spanish flag colors I want a vibrant eye catching design with the yellow / red colors over either Navy or white background or black even ,
Would like a 2D feel to the logo with another lighter color logo under it look ,

Contact Information for Business Card

Corvena Flooring
Tobin Reswick
Main Number
Cell Number
Fax Number

Website on the side of the card somewhere

Font styles to use
Sans Serif

Colors
ec1f27
ffc214

Requirements
Must have
• 2 logos feel one is bolder and the other one underneath very light

```html
<!DOCTYPE html>
<html lang="en">
<head>
<meta charset="utf-8">
<title>Corvena Card</title>
<link rel="stylesheet" href="https://fonts.googleapis.com/css2?family=Montserrat:wght@600;800&family=Poppins:wght@400&display=swap">
<style>
  :root {
    --backdrop: #3b3b3d;
    --navy: #12164a;
    --paper: #ffffff;
    --red: #ec1f27;
    --deep-red: #a3161b;
    --gold: #ffc214;
    --ink: #1d1d1f;
    --blush: #f3e9e4;
    --navy-faint: #1b2058;
  }
  html, body {
    margin: 0;
    width: 1200px;
    height: 900px;
    overflow: hidden;
    background: var(--backdrop);
  }
  .canvas {
    position: relative;
    width: 1200px;
    height: 900px;
  }
  .card {
    position: absolute;
    top: 295px;
    width: 540px;
    height: 310px;
    border-radius: 18px;
    overflow: hidden;
    box-shadow: 0 14px 30px rgba(0,0,0,0.45);
  }
  .card--front { left: 40px; background: var(--paper); }
  .card--back { left: 620px; background: var(--navy); }

  .faint-mark {
    position: absolute;
    background: var(--blush);
  }
  .card--front .faint-mark {
    right: -30px;
    bottom: -40px;
    width: 230px;
    height: 230px;
    transform: rotate(-8deg);
    opacity: 0.85;
  }
  .card--back .faint-mark {
    left: 170px;
    top: 55px;
    width: 200px;
    height: 200px;
    background: var(--navy-faint);
  }

  .brand {
    position: absolute;
    display: flex;
    flex-direction: column;
    align-items: center;
    gap: 12px;
  }
  .brand__square {
    width: 46px;
    height: 46px;
    background: var(--deep-red);
  }
  .card--back .brand__square { background: var(--red); }
  .brand__name {
    font-family: "Montserrat", sans-serif;
    font-weight: 600;
    font-size: 19px;
    letter-spacing: 4px;
    color: var(--gold);
    text-transform: uppercase;
    text-align: center;
    line-height: 1.3;
    margin: 0;
  }
  .card--front .brand { left: 30px; top: 95px; width: 210px; }
  .card--back .brand { left: 120px; top: 100px; width: 300px; }

  .divider {
    position: absolute;
    left: 262px;
    top: 80px;
    width: 1px;
    height: 140px;
    background: var(--deep-red);
  }
  .contact {
    position: absolute;
    left: 288px;
    top: 96px;
  }
  .contact__name {
    margin: 0 0 14px;
    font-family: "Montserrat", sans-serif;
    font-weight: 800;
    font-size: 19px;
    letter-spacing: 2px;
    color: var(--deep-red);
    text-transform: uppercase;
  }
  .contact__list {
    list-style: none;
    margin: 0;
    padding: 0;
  }
  .contact__item {
    display: flex;
    align-items: center;
    gap: 10px;
    margin-bottom: 8px;
    font-family: "Poppins", sans-serif;
    font-size: 13px;
    color: var(--ink);
  }
  .contact__icon {
    width: 18px;
    height: 18px;
    flex: none;
  }
</style>
</head>
<body>
<main class="canvas">
  <section class="card card--front">
    <div class="faint-mark" role="img" aria-label="Large faint brand mark in soft blush"></div>
    <div class="brand">
      <div class="brand__square"></div>
      <p class="brand__name">Corvena<br>Flooring</p>
    </div>
    <div class="divider"></div>
    <div class="contact">
      <h1 class="contact__name">Tobin Reswick</h1>
      <ul class="contact__list">
        <li class="contact__item">
          <svg class="contact__icon" viewBox="0 0 18 18"><rect x="3" y="3" width="12" height="12" transform="rotate(45 9 9)" fill="#a3161b"/><path d="M6.6 6.2l1.3-.4.8 1.8-.8.6c.4.9 1 1.5 1.9 1.9l.6-.8 1.8.8-.4 1.3c-2.6.2-5.4-2.6-5.2-5.2z" fill="#fff"/></svg>
          <span>0471-2283-5096</span>
        </li>
        <li class="contact__item">
          <svg class="contact__icon" viewBox="0 0 18 18"><rect x="3" y="3" width="12" height="12" transform="rotate(45 9 9)" fill="#a3161b"/><rect x="7" y="5.5" width="4" height="7" rx="0.8" fill="none" stroke="#fff" stroke-width="1"/></svg>
          <span>0428-6617-9034</span>
        </li>
        <li class="contact__item">
          <svg class="contact__icon" viewBox="0 0 18 18"><rect x="3" y="3" width="12" height="12" transform="rotate(45 9 9)" fill="#a3161b"/><rect x="5.5" y="6.5" width="7" height="5" fill="none" stroke="#fff" stroke-width="1"/><path d="M5.5 6.5L9 9.5l3.5-3" fill="none" stroke="#fff" stroke-width="1"/></svg>
          <span>hello@corvenaflooring.com</span>
        </li>
      </ul>
    </div>
  </section>

  <section class="card card--back">
    <div class="faint-mark" role="img" aria-label="Large faint brand mark in deep navy"></div>
    <div class="brand">
      <div class="brand__square"></div>
      <p class="brand__name">Corvena<br>Flooring</p>
    </div>
  </section>
</main>
</body>
</html>
```